Orbell Consulting- executive coaching business

looking for business card design for a newly started coaching business.
specialising in Exective coaching, Leadership, NLP and Motivation.
Looking for a simple, classy design using the existing logo attached and colour themes that complement the logo.
No red or orange in the business card design please.

Target Market(s)

Defence and Veteran community

Industry/Entity Type

Life Coaching

Contact Information for Business Card

looking for business cards for newly started coaching business.
specialising in Exective Coaching, Leadership, NLP and Motivation

Font styles to use
Serif
Script

Colors
0556a4
3176b5
86cfc6
33b8a4

Requirements
Must have
• Logo
• Email address- Jess@orbellconsulting.com.au
• Contact number
• Services provided - Executive Coaching, Leadership, NLP and Motivational Mapping.
Nice to have
• Same colours as logo
Should not have
• Red or orange

```html
<!DOCTYPE html>
<html lang="en">
<head>
<meta charset="utf-8">
<title>Orbell Consulting – Business Cards</title>
<link rel="stylesheet" href="https://fonts.googleapis.com/css2?family=Montserrat:wght@600&family=Noto+Serif:wght@700&family=Roboto:wght@400&display=swap">
<style>
  :root{
    --page:#e8e6e2;
    --card-black:#0c0c0d;
    --card-black-soft:#1a1a1c;
    --brand-blue:#0f6fbd;
    --white:#ffffff;
    --text-soft:#e6eef6;
    --ghost:#2a2a2d;
  }
  html,body{margin:0;padding:0;}
  body{
    width:1200px;height:892px;overflow:hidden;
    background:var(--page);
    position:relative;
    font-family:"Roboto",Arial,sans-serif;
  }
  .card{
    position:absolute;top:303px;
    width:500px;height:286px;
    border-radius:6px;overflow:hidden;
    background:linear-gradient(160deg,var(--card-black-soft),var(--card-black) 60%);
    box-shadow:0 10px 28px rgba(0,0,0,.28);
  }
  .card--front{left:60px;}
  .card--back{left:640px;}

  .front-bands{position:absolute;inset:0;}

  .brand{
    position:absolute;display:flex;align-items:center;gap:10px;
    font-family:"Montserrat",Arial,sans-serif;font-weight:600;
    color:var(--white);text-transform:uppercase;white-space:nowrap;
  }
  .brand__dot{border:2px solid var(--white);border-radius:50%;flex:none;}
  .card--front .brand{left:34px;top:52px;font-size:21px;letter-spacing:1px;gap:12px;}
  .card--front .brand__dot{width:36px;height:36px;}

  .contact{position:absolute;left:250px;top:150px;color:var(--white);}
  .contact__name{
    font-family:"Noto Serif",Georgia,serif;font-weight:700;
    font-size:19px;margin:0;
  }
  .contact__role{font-size:12.5px;margin:3px 0 16px;color:var(--text-soft);}
  .contact__line{display:flex;align-items:center;gap:10px;font-size:12.5px;margin:6px 0;}
  .contact__icon{width:14px;height:14px;flex:none;}

  .ghost-ring{
    position:absolute;left:170px;top:-10px;width:250px;height:250px;
    border:3px solid var(--ghost);border-radius:50%;
  }
  .divider{
    position:absolute;left:240px;top:0;width:1.5px;height:100%;
    background:rgba(255,255,255,.75);
  }
  .services{
    position:absolute;left:30px;top:88px;margin:0;padding:0;list-style:none;
    color:var(--white);font-size:13px;white-space:nowrap;
  }
  .services li{margin:0 0 18px;display:flex;align-items:center;gap:8px;}
  .services li::before{content:"";width:5px;height:5px;border-radius:50%;background:var(--white);}
  .card--back .brand{left:258px;top:124px;font-size:16px;letter-spacing:.5px;}
  .card--back .brand__dot{width:32px;height:32px;}
</style>
</head>
<body>

<section class="card card--front" aria-label="Business card front">
  <svg class="front-bands" width="500" height="286" viewBox="0 0 500 286" aria-hidden="true">
    <polygon points="0,250 355,112 410,0 500,0 500,286 0,286" fill="var(--brand-blue)"/>
    <polyline points="0,244 350,107 404,0" fill="none" stroke="var(--white)" stroke-width="4"/>
  </svg>
  <div class="brand">
    <span class="brand__dot"></span>
    <span class="brand__name">Orbell Consulting</span>
  </div>
  <div class="contact">
    <p class="contact__name">Daniel Hart</p>
    <p class="contact__role">Production Manager</p>
    <div class="contact__line">
      <svg class="contact__icon" viewBox="0 0 14 14" aria-hidden="true">
        <rect width="14" height="14" rx="2" fill="var(--white)"/>
        <path d="M4 3.5c.6 0 1.3 1.6 1.1 2-.2.4-.7.5-.4 1.1.4.8 1 1.4 1.8 1.8.6.3.7-.2 1.1-.4.4-.2 2 .5 2 1.1 0 .9-1 1.6-2 1.4C5.6 10 3.9 8.3 3.4 6.3 3.2 5.3 3.1 3.5 4 3.5z" fill="var(--brand-blue)"/>
      </svg>
      <span>+65 6000 4827</span>
    </div>
    <div class="contact__line">
      <svg class="contact__icon" viewBox="0 0 14 14" aria-hidden="true">
        <rect width="14" height="14" rx="2" fill="var(--white)"/>
        <rect x="3" y="4" width="8" height="6" fill="none" stroke="var(--brand-blue)" stroke-width="1.2"/>
        <polyline points="3,4 7,7.5 11,4" fill="none" stroke="var(--brand-blue)" stroke-width="1.2"/>
      </svg>
      <span>Jess@orbellconsulting.com.au</span>
    </div>
  </div>
</section>

<section class="card card--back" aria-label="Business card back">
  <div class="ghost-ring"></div>
  <ul class="services">
    <li>Executive Coaching</li>
    <li>Leadership</li>
    <li>NLP and Motivational Mapping.</li>
  </ul>
  <div class="divider"></div>
  <div class="brand">
    <span class="brand__name">Orbell Consulting</span>
    <span class="brand__dot"></span>
  </div>
</section>

</body>
</html>
```